Bakery Business Cards

We are in need of business cards for our bakery business--something non-generic that reflects our business and will stand out. We are a wholesale bakery that primarily services in-store bakeries, casinos, schools, distributors, and fund-raising companies. The family business was founded in 1960. (www.dorvalbakehouse.example)

```html
<!DOCTYPE html>
<html lang="en">
<head>
<meta charset="utf-8">
<title>Dorval Bakehouse – Business Cards</title>
<link href="https://fonts.googleapis.com/css2?family=Open+Sans:wght@400;600&display=swap" rel="stylesheet">
<style>
  :root {
    --backdrop: #333333;
    --brand-blue: #2b50a1;
    --ink-white: #ffffff;
  }
  html, body {
    margin: 0;
    padding: 0;
    width: 1200px;
    height: 1200px;
    overflow: hidden;
    background: var(--backdrop);
    font-family: "Open Sans", Arial, sans-serif;
  }
  .card {
    position: absolute;
    background: var(--brand-blue);
    color: var(--ink-white);
    overflow: hidden;
  }
  .card--front { left: 48px; top: 417px; width: 534px; height: 350px; }
  .card--back { left: 620px; top: 419px; width: 532px; height: 347px; }

  .brand {
    position: absolute;
    display: flex;
    align-items: flex-start;
    font-family: "Open Sans", Arial, sans-serif;
    font-weight: 600;
    color: var(--ink-white);
  }
  .brand__dot {
    border-radius: 50%;
    background: var(--ink-white);
    flex: none;
  }
  .brand__text { display: flex; flex-direction: column; align-items: flex-start; }
  .brand__line { display: block; line-height: 1.05; white-space: nowrap; }
  .brand__since { font-weight: 600; letter-spacing: 0.08em; text-transform: uppercase; white-space: nowrap; }

  .card--front .brand { left: 0; right: 0; top: 100px; justify-content: center; gap: 12px; }
  .card--front .brand__dot { width: 22px; height: 22px; margin-top: 12px; }
  .card--front .brand__line--first { font-size: 36px; }
  .card--front .brand__line--second { font-size: 48px; }
  .card--front .brand__since { font-size: 15px; margin-top: 8px; align-self: center; }

  .card--back .brand { left: 38px; top: 50px; gap: 8px; }
  .card--back .brand__dot { width: 13px; height: 13px; margin-top: 7px; }
  .card--back .brand__line--first { font-size: 20px; }
  .card--back .brand__line--second { font-size: 26px; }
  .card--back .brand__since { font-size: 9px; margin-top: 4px; align-self: center; }

  .photo {
    position: absolute;
    left: 0; top: 0;
    width: 532px; height: 347px;
  }

  .contact-list {
    position: absolute;
    left: 40px;
    top: 188px;
    margin: 0;
    padding: 0;
    list-style: none;
  }
  .contact-list__item {
    display: flex;
    align-items: center;
    height: 25px;
    margin-bottom: 9px;
    font-size: 16px;
    font-weight: 400;
    white-space: nowrap;
  }
  .contact-list__icon {
    width: 25px;
    height: 25px;
    margin-right: 8px;
    flex: none;
  }
</style>
</head>
<body>

<section class="card card--front" aria-label="Card front">
  <div class="brand">
    <span class="brand__dot"></span>
    <div class="brand__text">
      <span class="brand__line brand__line--first">Dorval</span>
      <span class="brand__line brand__line--second">Bakehouse</span>
      <span class="brand__since">Since 1960</span>
    </div>
  </div>
</section>

<section class="card card--back" aria-label="Card back">
  <svg class="photo" viewBox="0 0 532 347">
    <defs>
      <radialGradient id="pie-tones" cx="50%" cy="50%" r="60%">
        <stop offset="0%" stop-color="#d6a463"/>
        <stop offset="45%" stop-color="#e8dccb"/>
        <stop offset="75%" stop-color="#b98a55"/>
        <stop offset="100%" stop-color="#8e2a3c"/>
      </radialGradient>
    </defs>
    <circle cx="380" cy="100" r="172" fill="url(#pie-tones)" role="img" aria-label="Overhead photo of berry and apple pie slices on white plates on a wooden table"/>
  </svg>

  <div class="brand">
    <span class="brand__dot"></span>
    <div class="brand__text">
      <span class="brand__line brand__line--first">Dorval</span>
      <span class="brand__line brand__line--second">Bakehouse</span>
      <span class="brand__since">Since 1960</span>
    </div>
  </div>

  <ul class="contact-list">
    <li class="contact-list__item">
      <svg class="contact-list__icon" viewBox="0 0 25 25" aria-hidden="true">
        <circle cx="12.5" cy="12.5" r="12.5" fill="var(--ink-white)"/>
        <rect x="8.5" y="5.5" width="8" height="14" rx="1.5" fill="none" stroke="var(--brand-blue)" stroke-width="1.6"/>
        <circle cx="12.5" cy="16.8" r="0.9" fill="var(--brand-blue)"/>
      </svg>
      (555) 014-2290
    </li>
    <li class="contact-list__item">
      <svg class="contact-list__icon" viewBox="0 0 25 25" aria-hidden="true">
        <circle cx="12.5" cy="12.5" r="12.5" fill="var(--ink-white)"/>
        <rect x="6" y="8" width="13" height="9" rx="1" fill="none" stroke="var(--brand-blue)" stroke-width="1.6"/>
        <path d="M6.5 8.5 L12.5 13 L18.5 8.5" fill="none" stroke="var(--brand-blue)" stroke-width="1.6"/>
      </svg>
      orders@dorval.example
    </li>
    <li class="contact-list__item">
      <svg class="contact-list__icon" viewBox="0 0 25 25" aria-hidden="true">
        <circle cx="12.5" cy="12.5" r="12.5" fill="var(--ink-white)"/>
        <circle cx="12.5" cy="12.5" r="6.5" fill="none" stroke="var(--brand-blue)" stroke-width="1.5"/>
        <ellipse cx="12.5" cy="12.5" rx="3" ry="6.5" fill="none" stroke="var(--brand-blue)" stroke-width="1.3"/>
        <line x1="6" y1="12.5" x2="19" y2="12.5" stroke="var(--brand-blue)" stroke-width="1.3"/>
      </svg>
      www.dorvalbakehouse.example
    </li>
    <li class="contact-list__item">
      <svg class="contact-list__icon" viewBox="0 0 25 25" aria-hidden="true">
        <circle cx="12.5" cy="12.5" r="12.5" fill="var(--ink-white)"/>
        <path d="M12.5 20 C9 15.5 7.5 13 7.5 10.5 A5 5 0 0 1 17.5 10.5 C17.5 13 16 15.5 12.5 20 Z" fill="var(--brand-blue)"/>
        <circle cx="12.5" cy="10.5" r="2" fill="var(--ink-white)"/>
      </svg>
      1870 Meridian Row, Fairview, OK 73000
    </li>
  </ul>
</section>

</body>
</html>
```